Velvet Harbor Powerpoint Presentation

Looking for powerpoint presentation template for our boutique social media management and digital marketing company.
We will be using this Powerpoint template for presentations, guest speaking sessions and proposals.
We need a front page and then a few different versions of what the rest of the template would look like.
I have attached our business cards, different versions of our logo, and our PDF so you can get a look at our identity and get a feel of what we are about. Our website will be up in about two weeks.
Target Market(s)
Small to medium size business owners (all different catagories)
Industry/Entity Type
Marketing
Requirements
Must have
- The logo
- a very boutique, high end look. You will see what I mean when you look at our business cards and our PDF.
- We only want to use the Velvet Harbor colors- Black, White, Rose Gold and Grey
Should not have
- Lot's of colors that are not part of the Velvet Harbor identity

```html
<!DOCTYPE html>
<html lang="en">
<head>
<meta charset="utf-8">
<title>Velvet Harbor Presentation Template</title>
<link href="https://fonts.googleapis.com/css2?family=Bebas+Neue&family=Open+Sans:wght@400;600;700&family=Raleway:wght@300&display=swap" rel="stylesheet">
<style>
:root{
  --ink:#2b2b2b;
  --charcoal:#333333;
  --grey:#595959;
  --grey-soft:#8a8a8a;
  --rose:#df7f5f;
  --rose-mid:#e8a288;
  --rose-pale:#f9e7e0;
  --white:#ffffff;
  --page:#ffffff;
}
*{box-sizing:border-box;margin:0;padding:0}
html,body{width:870px;height:1200px;overflow:hidden;background:var(--page)}
body{position:relative;font-family:'Open Sans',sans-serif;color:var(--grey)}
.slide{position:absolute;width:296px;height:222px;overflow:hidden;background:var(--white);box-shadow:0 2px 6px rgba(0,0,0,.25)}
.abs{position:absolute}
.photo{position:absolute}
.head{font-family:'Bebas Neue',sans-serif;letter-spacing:.3px;line-height:1}
.tiny{font-size:3.6px;line-height:5px;color:var(--grey-soft)}
/* positions */
.s1{left:120px;top:105px}.s2{left:457px;top:105px}
.s3{left:120px;top:361px}.s4{left:457px;top:361px}
.s5{left:120px;top:616px}.s6{left:457px;top:616px}
.s7{left:120px;top:868px}.s8{left:457px;top:868px}

/* cover */
.s1 .photo{inset:0;background:linear-gradient(90deg,#5d6f86 0%,#b7c3cf 30%,#dfe6ec 60%,#6d7480 80%,#c9ced4 100%)}
.cover-panel{position:absolute;left:109px;top:0;width:115px;height:222px;background:var(--ink)}
.brand{position:absolute;top:52px;width:100%;text-align:center;color:var(--rose-mid)}
.brand .mark{width:14px;height:14px;border:1px solid var(--rose-mid);border-radius:50%;margin:0 auto 5px}
.brand .name{font-family:'Raleway',sans-serif;font-weight:300;font-size:9px;letter-spacing:.5px}
.people{position:absolute;top:168px;width:100%;text-align:center;color:#bdbdbd;font-size:3.6px;line-height:4.6px}
.people p+p{margin-top:4px}

/* icon card */
.s2 .photo{inset:0;background:linear-gradient(90deg,#4a4a4a 0%,#7c7f82 50%,#c8ccce 100%)}
.s2 .shade{position:absolute;left:0;top:0;width:116px;height:222px;background:rgba(60,60,60,.75)}
.s2 .lead{position:absolute;left:14px;top:42px;width:90px;color:var(--white);font-size:7.2px;line-height:9.6px;text-align:center}
.s2 .card{position:absolute;left:116px;top:15px;width:145px;height:192px;background:var(--white);padding:14px 10px 0;text-align:center}
.s2 .item{height:58px}
.s2 .item svg{display:block;margin:0 auto 5px}

/* photo + text */
.s3 .band{position:absolute;left:0;top:173px;width:296px;height:49px;background:var(--grey)}
.s3 .photo{left:18px;top:32px;width:108px;height:162px;background:linear-gradient(160deg,#c7d3dc,#5d6b7c 60%,#2f3a4a)}
.s3 .title{left:141px;top:28px;font-size:15px;color:var(--charcoal)}
.s3 .sub{left:141px;top:46px;font-size:5.5px;color:var(--rose);font-weight:600}
.s3 ul{position:absolute;left:148px;top:63px;font-size:4.4px;line-height:5.6px;color:var(--grey)}
.s3 .label{left:141px;top:99px;font-size:4.4px;color:var(--rose);font-weight:600}
.s3 .body{left:141px;top:109px;width:138px;font-size:4.2px;line-height:5.6px;color:var(--grey)}
.s3 .foot{left:155px;top:188px;font-size:11px;color:var(--white)}

/* team */
.s4 .band{position:absolute;left:0;top:114px;width:296px;height:108px;background:var(--grey)}
.s4 .title{left:0;width:100%;top:24px;text-align:center;font-size:17px;color:var(--charcoal)}
.member{position:absolute;top:78px;width:80px;margin-left:-40px;text-align:center}
.member .avatar{width:68px;height:68px;margin:0 auto;border-radius:50%;border:2px solid var(--rose-mid);background:radial-gradient(circle at 50% 45%,#c9bcb3,#6d6864)}
.member .nm{font-family:'Bebas Neue',sans-serif;font-size:8.5px;color:var(--white);margin-top:5px}
.member .rl{font-size:4px;color:#ddd}

/* quality */
.s5 .photo{inset:0;background:linear-gradient(135deg,#1f2e47,#3e5474 45%,#1b2638)}
.s5 .title{left:0;width:100%;top:27px;text-align:center;font-size:12.5px;color:var(--white)}
.s5 .card{position:absolute;left:34px;top:53px;width:232px;height:149px;background:var(--white)}
.s5 .card .photo{left:0;top:0;width:116px;height:149px;background:linear-gradient(150deg,#e9eef2,#a9b7c4 55%,#3c4a5e)}
.s5 .q{left:160px;top:20px;font-size:12px;color:var(--rose)}
.s5 ul{position:absolute;left:142px;top:48px;width:84px;font-size:4.2px;line-height:5.6px;color:var(--grey);padding-left:6px}

/* three pillars */
.s6 .photo{inset:0;background:linear-gradient(180deg,#4b4b4b 0%,#7a7a7a 45%,#b9b4ae 100%)}
.s6 .title{left:0;width:100%;top:28px;text-align:center;font-size:14.5px;line-height:15.5px;color:var(--white)}
.s6 .card{position:absolute;left:30px;top:87px;width:238px;height:135px;background:var(--white);display:flex;justify-content:space-around;padding:15px 6px 0}
.s6 .col{width:66px;text-align:center}
.s6 .col svg{display:block;margin:0 auto 6px}
.s6 .col h4{font-size:4.6px;font-weight:600;color:var(--grey);margin-bottom:4px}
.s6 .col p{font-size:3.8px;line-height:4.8px;color:var(--grey);font-weight:600}

/* steps */
.s7 .title{left:0;width:100%;top:27px;text-align:center;font-size:17.5px;color:var(--charcoal)}
.s7 .sub{left:0;width:100%;top:48px;text-align:center;font-family:'Bebas Neue',sans-serif;font-size:6.5px;color:var(--charcoal)}
.steps{position:absolute;left:21px;top:71px;width:141px}
.step{display:flex;height:27px;margin-bottom:3px;background:var(--rose-pale)}
.step .num{width:22px;display:flex;align-items:center;justify-content:center;color:var(--white);font-weight:700;font-size:7px}
.step:nth-child(1) .num{background:var(--rose-mid)}
.step:nth-child(2) .num{background:var(--rose)}
.step:nth-child(3) .num{background:var(--rose-mid)}
.step:nth-child(4) .num{background:var(--rose)}
.step .txt{padding:4px 0 0 4px}
.step b{display:block;font-size:4.4px;color:var(--charcoal)}
.step .tiny{font-size:3.2px;line-height:4.2px}
.s7 .photo{left:169px;top:71px;width:112px;height:117px;background:linear-gradient(145deg,#dfe9f2,#7f9bb8 50%,#2c4766)}

/* services */
.s8 .title{left:0;width:100%;top:22px;text-align:center;font-size:15px;color:var(--charcoal)}
.svc{position:absolute;top:65px;width:123px;height:129px;background:var(--rose-pale);border-bottom:1.5px solid var(--rose)}
.svc h5{height:18px;line-height:18px;text-align:center;color:var(--white);font-size:5.2px;font-weight:600}
.svc p{padding:24px 6px 0;text-align:center;font-size:5.8px;line-height:8.8px;color:var(--grey)}
.svc.a{left:22px}.svc.a h5{background:var(--rose)}
.svc.b{left:156px}.svc.b h5{background:var(--rose-mid)}
</style>
</head>
<body>

<section class="slide s1">
  <div class="photo" role="img" aria-label="Business people shaking hands in a bright office"></div>
  <div class="cover-panel">
    <div class="brand"><div class="mark"></div><div class="name">VELVET HARBOR</div></div>
    <div class="people">
      <p>NORA ELLIS<br>Co-Founder &amp; CEO<br>(555) 010-2841</p>
      <p>CLARA VOSS<br>Co-Founder &amp; CEO<br>(555) 010-3397</p>
    </div>
  </div>
</section>

<section class="slide s2">
  <div class="photo" role="img" aria-label="Bright modern office interior with tall windows"></div>
  <div class="shade"></div>
  <p class="lead"><b>Lorem ipsum dolor sit amet consectetur adipiscing elit. Cras bibendum mattis leo, ac efficitur ipsum lobortis non. Praesent vitae pulvinar</b> Lorem ipsum dolor sit amet consectetur adipiscing elit. Cras bibendum mattis leo, ac efficitur ipsum lobortis non. Praesent vitae pulvinar</p>
  <div class="card">
    <div class="item">
      <svg width="20" height="16" viewBox="0 0 20 16"><rect x="7" y="0.5" width="6" height="3" fill="none" stroke="#df7f5f"/><rect x="0" y="3" width="20" height="13" rx="1.5" fill="#e8a288"/><rect x="0" y="8" width="20" height="1.2" fill="#fff"/><rect x="8.5" y="7" width="3" height="3" fill="#df7f5f"/></svg>
      <p class="tiny">Lorem ipsum dolor sit amet consectetur adipiscing elit. Cras bibendum mattis leo, ac efficitur ipsum lobortis non. Praesent vitae pulvinar metus. Phasellus accumsan elementum condimentum. Nullam rutrum, tellus</p>
    </div>
    <div class="item">
      <svg width="22" height="16" viewBox="0 0 22 16"><rect x="0.5" y="0.5" width="21" height="15" rx="1.5" fill="none" stroke="#df7f5f"/><rect x="0.5" y="0.5" width="21" height="3" fill="#e8a288"/><g fill="#df7f5f"><rect x="4" y="6" width="14" height="1.3"/><rect x="4" y="9" width="14" height="1.3"/><rect x="4" y="12" width="14" height="1.3"/></g></svg>
      <p class="tiny">Lorem ipsum dolor sit amet consectetur adipiscing elit. Cras bibendum mattis leo, ac efficitur ipsum lobortis non. Praesent vitae pulvinar metus. Phasellus accumsan elementum condimentum. Nullam rutrum, tellus</p>
    </div>
    <div class="item">
      <svg width="24" height="18" viewBox="0 0 24 18"><circle cx="8" cy="11" r="5.5" fill="none" stroke="#e8a288" stroke-width="3" stroke-dasharray="2.5 1.6"/><circle cx="18" cy="5" r="3.8" fill="none" stroke="#e8a288" stroke-width="2.4" stroke-dasharray="2 1.3"/></svg>
      <p class="tiny">Lorem ipsum dolor sit amet consectetur adipiscing elit. Cras bibendum mattis leo, ac efficitur ipsum lobortis non. Praesent vitae pulvinar metus. Phasellus accumsan elementum condimentum. Nullam rutrum, tellus</p>
    </div>
  </div>
</section>

<section class="slide s3">
  <div class="band"></div>
  <div class="photo" role="img" aria-label="Smiling business team standing together"></div>
  <h2 class="abs head title">LOREM IPSUM DOLOR SIT</h2>
  <p class="abs sub">LOREM IPSUM DOLOR</p>
  <ul>
    <li>Lorem ipsum dolor sit amet</li>
    <li>consectetur adipiscing elit</li>
    <li>Cras bibendum mattis leo, ac</li>
    <li>efficitur ipsum lobortis non</li>
  </ul>
  <p class="abs label">Lorem ipsum dolor:</p>
  <p class="abs body">Lorem ipsum dolor sit amet consectetur adipiscing elit. Cras bibendum mattis leo, ac efficitur ipsum lobortis non. Praesent vitae pulvinar metus. Phasellus accumsan elementum condimentum. Nullam rutrum, tellus tincidunt scelerisque placerat, justo lectus luctus odio, varius auctor urna lacus sed nisl. Suspendisse et placerat sem. Duis tincidunt augue vel eros hendrerit tempus.</p>
  <p class="abs head foot">LOREM IPSUM DOLOR SIT</p>
</section>

<section class="slide s4">
  <div class="band"></div>
  <h2 class="abs head title">OUT TEAM MEMBERS</h2>
  <div class="member" style="left:69px"><div class="avatar" role="img" aria-label="Team member portrait"></div><p class="nm">LOREM IPSUM</p><p class="rl">LOREM IPSUM</p></div>
  <div class="member" style="left:148px"><div class="avatar" role="img" aria-label="Team member portrait"></div><p class="nm">LOREM IPSUM</p><p class="rl">LOREM IPSUM</p></div>
  <div class="member" style="left:229px"><div class="avatar" role="img" aria-label="Team member portrait"></div><p class="nm">LOREM IPSUM</p><p class="rl">LOREM IPSUM</p></div>
</section>

<section class="slide s5">
  <div class="photo" role="img" aria-label="Looking up at glass office towers"></div>
  <h2 class="abs head title">LOREM IPSUM DOLOR SIT AMET CONSECTETUR</h2>
  <div class="card">
    <div class="photo" role="img" aria-label="Colleagues smiling around a laptop"></div>
    <h3 class="abs head q">QUALITY</h3>
    <ul>
      <li>Lorem ipsum dolor sit amet consectetur adipiscing elit. Cras</li>
      <li>Lorem ipsum dolor sit amet consectetur adipiscing elit. Cras</li>
      <li>Lorem ipsum dolor sit amet consectetur adipiscing elit. Cras</li>
      <li>Lorem ipsum dolor sit amet consectetur adipiscing elit. Cras</li>
      <li>Lorem ipsum dolor sit amet consectetur adipiscing elit. Cras</li>
    </ul>
  </div>
</section>

<section class="slide s6">
  <div class="photo" role="img" aria-label="Blurred office corridor with people walking"></div>
  <h2 class="abs head title">LOREM IPSUM DOLOR SIT AMET<br>CONSECTETUR ADIPISCING ELIT.</h2>
  <div class="card">
    <div class="col">
      <svg width="20" height="20" viewBox="0 0 20 20"><rect x="1" y="1" width="18" height="14" rx="2" fill="#e8a288"/><circle cx="7" cy="9" r="3" fill="#fff"/><circle cx="13" cy="9" r="3" fill="#fff"/><path d="M7 15 L10 19 L13 15Z" fill="#e8a288"/></svg>
      <h4>LOREM IPSUM</h4>
      <p>Lorem ipsum dolor sit amet consectetur adipiscing elit. Cras bibendum mattis leo, ac efficitur ipsum lobortis non. Praesent vitae pulvinar metus. Phasellus accumsan elementum condimentum. Nullam rutrum, tellus tincidunt scelerisque elementum</p>
    </div>
    <div class="col">
      <svg width="22" height="20" viewBox="0 0 22 20"><path d="M11 1 L21 6 H1Z" fill="#e8a288"/><g fill="#e8a288"><rect x="3" y="8" width="2" height="8"/><rect x="7.5" y="8" width="2" height="8"/><rect x="12.5" y="8" width="2" height="8"/><rect x="17" y="8" width="2" height="8"/><rect x="1" y="17" width="20" height="2"/></g></svg>
      <h4>LOREM IPSUM</h4>
      <p>Lorem ipsum dolor sit amet consectetur adipiscing elit. Cras bibendum mattis leo, ac efficitur ipsum lobortis non. Praesent vitae pulvinar metus. Phasellus accumsan elementum condimentum. Nullam rutrum, tellus tincidunt scelerisque elementum</p>
    </div>
    <div class="col">
      <svg width="22" height="20" viewBox="0 0 22 20"><path d="M1 4 H8 L10 6 H20 V17 H1Z" fill="#e8a288"/><path d="M4 9 H21 L18 17 H1Z" fill="#df7f5f"/></svg>
      <h4>LOREM IPSUM</h4>
      <p>Lorem ipsum dolor sit amet consectetur adipiscing elit. Cras bibendum mattis leo, ac efficitur ipsum lobortis non. Praesent vitae pulvinar metus. Phasellus accumsan elementum condimentum. Nullam</p>
    </div>
  </div>
</section>

<section class="slide s7">
  <h2 class="abs head title">LOREM IPSUM DOLOR SIT AMET</h2>
  <p class="abs sub">CONSECTETUR ADIPISCING ELIT. CRAS</p>
  <div class="steps">
    <div class="step"><div class="num">01</div><div class="txt"><b>Lorem ipsum dolor sit amet</b><p class="tiny">Lorem ipsum dolor sit amet consectetur adipiscing elit.<br>Cras bibendum mattis leo. Lorem ipsum dolor sit amet</p></div></div>
    <div class="step"><div class="num">02</div><div class="txt"><b>Lorem ipsum dolor sit amet</b><p class="tiny">Lorem ipsum dolor sit amet consectetur adipiscing elit.<br>Cras bibendum mattis leo. Lorem ipsum dolor sit amet</p></div></div>
    <div class="step"><div class="num">03</div><div class="txt"><b>Lorem ipsum dolor sit amet</b><p class="tiny">Lorem ipsum dolor sit amet consectetur adipiscing elit.<br>Cras bibendum mattis leo. Lorem ipsum dolor sit amet</p></div></div>
    <div class="step"><div class="num">04</div><div class="txt"><b>Lorem ipsum dolor sit amet</b><p class="tiny">Lorem ipsum dolor sit amet consectetur adipiscing elit.<br>Cras bibendum mattis leo. Lorem ipsum dolor sit amet</p></div></div>
  </div>
  <div class="photo" role="img" aria-label="Hand using a tablet over printed charts"></div>
</section>

<section class="slide s8">
  <h2 class="abs head title">OUR SERVICES</h2>
  <div class="svc a"><h5>LOREM IPSUM</h5><p>Lorem ipsum dolor sit amet consectetur adipiscing elit. Cras bibendum mattis leo, ac efficitur ipsum lobortis non. Praesent vitae pulvinar metus. Phasellus accumsan elementum condimentum. Nullam rutrum, tellus tincidunt scelerisque elementum</p></div>
  <div class="svc b"><h5>LOREM IPSUM</h5><p>Lorem ipsum dolor sit amet consectetur adipiscing elit. Cras bibendum mattis leo, ac efficitur ipsum lobortis non. Praesent vitae pulvinar metus. Phasellus accumsan elementum condimentum. Nullam rutrum, tellus tincidunt scelerisque elementum</p></div>
</section>

</body>
</html>
```